Mental Health & Addiction Podcast Art

Project: Podcast Cover Art / Visual Identity
Podcast Name: The Renewal Compass
Focus: Recovery from substance use and mental health
Objectives
Create compelling podcast artwork that:
Reflects the themes of hope, healing, and personal growth
Establishes credibility and professionalism
Appeals to individuals seeking recovery resources and support
Maintains strong brand consistency with Harborline Wellness
Brand Integration Requirements
Logo incorporation: Integrate an element from the Harborline Wellness Logo—potentially an abstract or partial use of the sun motif
Flexibility: Open to creative interpretations (e.g., sun rays as background texture, sunrise gradient, partial sun as a design accent)
Mandatory: Must adhere to existing Harborline Wellness brand guidelines (approved color palette, typography, and visual style)

Target Market(s)

United states, people with addiction and mental health disorders.

Industry/Entity Type

Wellness

Font styles to use
Other font styles liked:
• See Brand Guide

Requirements
Must have
• Match brand guide, in corporate elements of the Harborline Wellness Logo icon

```html
<!DOCTYPE html>
<html lang="en">
<head>
<meta charset="utf-8">
<title>The Renewal Compass – Podcast Cover Options</title>
<link rel="stylesheet" href="https://fonts.googleapis.com/css2?family=Source+Serif+4:opsz,wght@8..60,700&family=IBM+Plex+Sans:wght@400&display=swap">
<style>
  :root {
    --canvas-grey: #c8c9cb;
    --sun-gold: #f7b533;
    --warm-sand: #fbd58a;
    --mist-sage: #d9d6b8;
    --sea-glass: #c4dfe0;
    --sky-blue: #a9def3;
    --deep-teal: #0c4a5e;
    --sun-white: #ffffff;
  }
  * { margin: 0; padding: 0; box-sizing: border-box; }
  html, body {
    width: 941px;
    height: 1200px;
    overflow: hidden;
    background: var(--canvas-grey);
  }
  .canvas {
    position: relative;
    width: 941px;
    height: 1200px;
  }
  .cover {
    position: absolute;
    left: 102px;
    width: 420px;
    height: 420px;
    overflow: hidden;
    color: var(--deep-teal);
    box-shadow: -10px 6px 10px -6px rgba(0,0,0,0.25);
  }
  .cover--wide { top: 123px; }
  .cover--stacked { top: 685px; }
  .cover__wash {
    position: absolute;
    inset: 0;
    background: linear-gradient(180deg,
      var(--sun-gold) 0%,
      var(--warm-sand) 22%,
      var(--warm-sand) 38%,
      var(--mist-sage) 58%,
      var(--sea-glass) 76%,
      var(--sky-blue) 100%);
  }
  .brand-mark {
    position: absolute;
    display: flex;
    align-items: center;
    gap: 12px;
    white-space: nowrap;
  }
  .brand-mark__dot {
    width: 54px;
    height: 54px;
    border-radius: 50%;
    background: var(--sun-white);
  }
  .brand-mark__name {
    font-family: "Source Serif 4", Georgia, serif;
    font-weight: 700;
    font-size: 20px;
    color: var(--sun-white);
  }
  .cover--wide .brand-mark { left: 112px; top: 112px; }
  .cover--stacked .brand-mark { left: 122px; top: 82px; }
  .cover__title {
    position: absolute;
    left: 25px;
    font-family: "Source Serif 4", Georgia, serif;
    font-weight: 700;
    line-height: 0.92;
    letter-spacing: -0.3px;
  }
  .cover__subtitle {
    position: absolute;
    left: 25px;
    font-family: "IBM Plex Sans", Arial, sans-serif;
    font-weight: 400;
  }
  .cover--wide .cover__title { top: 234px; font-size: 43px; }
  .cover--wide .cover__subtitle { top: 322px; font-size: 21.5px; line-height: 27px; }
  .cover--stacked .cover__title { top: 193px; font-size: 50px; line-height: 0.9; }
  .cover--stacked .cover__subtitle { top: 333px; font-size: 24px; line-height: 31px; }
</style>
</head>
<body>
  <main class="canvas">
    <section class="cover cover--wide" aria-label="Podcast cover, two-line title">
      <div class="cover__wash" role="img" aria-label="Sunrise watercolour wash from golden yellow to soft sky blue"></div>
      <div class="brand-mark">
        <span class="brand-mark__dot"></span>
        <span class="brand-mark__name">Harborline Wellness</span>
      </div>
      <h1 class="cover__title">The<br>Renewal Compass</h1>
      <p class="cover__subtitle">Recovery from substance use<br>and mental health</p>
    </section>

    <section class="cover cover--stacked" aria-label="Podcast cover, three-line title">
      <div class="cover__wash" role="img" aria-label="Sunrise watercolour wash from golden yellow to soft sky blue"></div>
      <div class="brand-mark">
        <span class="brand-mark__dot"></span>
        <span class="brand-mark__name">Harborline Wellness</span>
      </div>
      <h1 class="cover__title">The<br>Renewal<br>Compass</h1>
      <p class="cover__subtitle">Recovery from substance use<br>and mental health</p>
    </section>
  </main>
</body>
</html>
```